MossVane Spa, Skincare and Cosmetics website

I need a website for MossVane (putting the glow back into people's skin) which allows viewers to access information about Beauty Spa packaging and facilities as well as online skincare and cosmetic products. Our distinctive difference is that our products are certified organic. We want to target a luxury high income niche market (age 30-50). I want all colours to be "baby colours" preferably background to be "baby metallic pink" (but please don't make the website too immature) with curves as patterns. I want a romantic vintage look.

The website needs to look:
1. elegant (prestige and luxury)
2. bright (baby colours mainly)
3. European curves and signature patterns
4. Can include Pearl related pics (but not a must)

The website pages needs to have:
1. pages ordering skincare/cosmetics
2. shopping cart and payment
3. about us and about our product differences
4. contact us
5. booking for spa treatments and packages

I have attached our logo and also packaging label styles.

Industry/Entity Type

Cosmetics

```html
<!DOCTYPE html>
<html lang="en">
<head>
<meta charset="utf-8">
<title>MossVane Spa, Skincare and Cosmetics</title>
<link rel="stylesheet" href="https://fonts.googleapis.com/css2?family=Roboto+Condensed:wght@400;700&display=swap">
<style>
  :root {
    --plum-dark: #2e2731;
    --plum-band: #564858;
    --rose: #c7a094;
    --rose-soft: #e9d6cf;
    --ink: #4a4248;
    --muted: #8c8389;
    --white: #ffffff;
    --page: #f1eff0;
    --hero-a: #e8d7cc;
    --hero-b: #b9a193;
    --hero-c: #5f8a4a;
  }
  * { box-sizing: border-box; margin: 0; padding: 0; }
  html, body { width: 1200px; height: 800px; overflow: hidden; }
  body {
    background: var(--page);
    font-family: "Roboto Condensed", Arial, sans-serif;
    color: var(--ink);
  }
  .site { width: 1200px; height: 800px; display: flex; flex-direction: column; }
  .container { width: 1040px; margin: 0 auto; }

  .top-nav { background: var(--plum-dark); height: 38px; }
  .top-nav .container { height: 100%; display: flex; align-items: center; justify-content: space-between; }
  .menu { display: flex; list-style: none; gap: 26px; }
  .menu a { color: var(--white); text-decoration: none; font-size: 12px; letter-spacing: .3px; }
  .menu a.is-current { color: var(--rose-soft); }
  .social { display: flex; gap: 9px; }
  .social span { width: 10px; height: 10px; border-radius: 50%; background: #cfc7cc; }

  .masthead { background: var(--white); height: 104px; }
  .masthead .container { height: 100%; display: flex; align-items: center; justify-content: space-between; }
  .contact-item { display: flex; align-items: center; gap: 7px; font-size: 13px; color: var(--ink); width: 200px; }
  .contact-item.phone { justify-content: flex-end; }
  .brand { display: flex; flex-direction: column; align-items: center; gap: 6px; }
  .brand-dot { width: 22px; height: 22px; border-radius: 50%; background: var(--rose); }
  .brand-name { font-size: 26px; letter-spacing: 3px; color: var(--rose); font-weight: 400; text-transform: uppercase; }

  .hero {
    height: 368px;
    background: linear-gradient(90deg, var(--hero-a) 0%, var(--hero-b) 45%, #8e7a6c 62%, var(--hero-c) 80%, #b9ab9c 100%);
  }

  .intro-band { background: var(--plum-band); height: 92px; }
  .intro-band .container { height: 100%; display: flex; align-items: center; }
  .intro-band p { color: #e7dfe4; font-size: 13px; line-height: 1.6; max-width: 1000px; }

  .features { background: var(--white); flex: 1; }
  .features .container { height: 100%; display: flex; justify-content: space-between; align-items: center; }
  .feature { width: 240px; display: flex; flex-direction: column; align-items: center; gap: 10px; }
  .feature-icon { width: 46px; height: 46px; border-radius: 50%; background: #e6e2e4; display: flex; align-items: center; justify-content: center; }
  .feature-title { font-size: 15px; color: var(--ink); }
</style>
</head>
<body>
<div class="site">
  <nav class="top-nav">
    <div class="container">
      <ul class="menu">
        <li><a class="is-current" href="#">Home</a></li>
        <li><a href="#">About</a></li>
        <li><a href="#">Spa &amp; Treatments</a></li>
        <li><a href="#">Products</a></li>
        <li><a href="#">Booking</a></li>
        <li><a href="#">News &amp; Blog</a></li>
        <li><a href="#">Your Cart</a></li>
        <li><a href="#">Contact</a></li>
      </ul>
      <div class="social" aria-label="Social links">
        <span></span><span></span><span></span><span></span><span></span><span></span>
      </div>
    </div>
  </nav>

  <header class="masthead">
    <div class="container">
      <div class="contact-item location">
        <svg width="10" height="14" viewBox="0 0 10 14" aria-hidden="true"><path d="M5 0a5 5 0 0 0-5 5c0 3.5 5 9 5 9s5-5.5 5-9a5 5 0 0 0-5-5zm0 7a2 2 0 1 1 0-4 2 2 0 0 1 0 4z" fill="#6d6469"/></svg>
        <span>Larkmoor, CA</span>
      </div>
      <div class="brand">
        <span class="brand-dot"></span>
        <span class="brand-name">MossVane</span>
      </div>
      <div class="contact-item phone">
        <svg width="12" height="12" viewBox="0 0 12 12" aria-hidden="true"><path d="M2.5 0.5l2 2.3-1.2 1.5c.7 1.6 2 2.9 3.6 3.6l1.5-1.2 2.3 2-1 2.3C4.6 11 1 7.4.2 2.3z" fill="#6d6469"/></svg>
        <span>+1 (415) 555-0198</span>
      </div>
    </div>
  </header>

  <section class="hero" role="img" aria-label="Photo of guests in white towels relaxing together in a spa lounge with green walls"></section>

  <section class="intro-band">
    <div class="container">
      <p>Unwind in a calm retreat where every ritual is built around certified organic care. Our therapists pair gentle massage with botanical oils, soft light and quiet rooms, so your skin and mind leave rested. Book a single treatment or a full day package, then carry the glow home with our skincare range.</p>
    </div>
  </section>

  <section class="features">
    <div class="container">
      <div class="feature">
        <span class="feature-icon"><svg width="22" height="22" viewBox="0 0 22 22" aria-hidden="true"><path d="M11 3c4 4 4 12 0 16-4-4-4-12 0-16z" fill="#8c8389"/></svg></span>
        <span class="feature-title">Full Service Spa</span>
      </div>
      <div class="feature">
        <span class="feature-icon"><svg width="22" height="22" viewBox="0 0 22 22" aria-hidden="true"><rect x="7" y="6" width="8" height="12" rx="2" fill="#8c8389"/><rect x="9" y="3" width="4" height="3" fill="#8c8389"/></svg></span>
        <span class="feature-title">Vitality Products</span>
      </div>
      <div class="feature">
        <span class="feature-icon"><svg width="22" height="22" viewBox="0 0 22 22" aria-hidden="true"><rect x="4" y="9" width="14" height="10" fill="#8c8389"/><rect x="3" y="6" width="16" height="3" fill="#8c8389"/><rect x="10" y="6" width="2" height="13" fill="#e6e2e4"/></svg></span>
        <span class="feature-title">The Perfect Gift</span>
      </div>
      <div class="feature">
        <span class="feature-icon"><svg width="22" height="22" viewBox="0 0 22 22" aria-hidden="true"><path d="M3 5h16v9H9l-4 3v-3H3z" fill="#8c8389"/></svg></span>
        <span class="feature-title">Consultations</span>
      </div>
    </div>
  </section>
</div>
</body>
</html>
```